Job application set/company logo

My resume, profile and project file need to be designed in a common, fresh business design, not too playful and colourful
Potentially a logo for my company called Quill Brook Consulting needs to be designed in a second step. My company is consulting in digitalization and business transformation.

```html
<!DOCTYPE html>
<html lang="en">
<head>
<meta charset="utf-8">
<title>Marcus Vellinger – Resume</title>
<link href="https://fonts.googleapis.com/css2?family=Oswald:wght@500&family=Source+Sans+3:ital,wght@0,300;0,400;0,600;0,700;1,400;1,600&display=swap" rel="stylesheet">
<style>
:root{
  --backdrop:#ababab;
  --navy:#333a4b;
  --ink:#262c3b;
  --paper:#ffffff;
  --light:#eef0f4;
  --muted:#c9ccd5;
  --rule:#5b6172;
}
*{box-sizing:border-box;margin:0;padding:0}
html,body{width:1200px;height:904px;overflow:hidden;background:var(--backdrop)}
body{position:relative;font-family:"Source Sans 3",Arial,sans-serif;color:var(--ink)}
ul{list-style:none}
a{color:inherit;text-decoration:none}

.page{position:absolute;top:105px;width:491px;height:694px;background:var(--navy)}
.page--one{left:85px}
.page--two{left:624px}
.sheet{position:absolute;left:197px;top:20px;width:294px;height:668px;background:var(--paper)}

/* sidebar */
.portrait-ring{position:absolute;left:20px;top:22px;width:155px;height:155px;border-radius:50%;border:1.5px solid var(--light)}
.portrait{position:absolute;left:6px;top:6px;width:140px;height:140px;border-radius:50%;background:radial-gradient(circle at 50% 40%,#d9d5cf 0%,#9a9893 45%,#2e2f35 100%)}
.name{position:absolute;left:25px;top:195px;width:160px;font-family:"Oswald","Arial Narrow",sans-serif;font-weight:500;font-size:21.5px;line-height:24px;color:var(--paper);letter-spacing:-.3px;white-space:nowrap}
.side-tab{position:absolute;left:25.5px;width:120px;height:19.5px;background:var(--paper);border-radius:0 10px 10px 0;color:var(--navy);font-weight:700;font-size:11.6px;line-height:19.5px;padding-left:7px;letter-spacing:.1px}
.info-row{position:absolute;left:26px;display:flex;gap:5px;align-items:flex-start;color:var(--light);font-size:8.8px;line-height:10.9px;font-weight:600}
.info-row svg{flex:none;width:9px;height:9px;margin-top:1px}
.side-head{position:absolute;left:25.5px;color:var(--paper);font-weight:600;font-size:11px;line-height:12px;letter-spacing:.1px}
.side-list{position:absolute;left:25.5px;width:160px;border-left:1px dotted var(--muted);padding-left:7px;color:var(--light);font-size:8.9px;line-height:10.9px;font-weight:300}
.side-list li{position:relative;margin-bottom:7px}
.side-list li::before{content:"";position:absolute;left:-9.3px;top:3.5px;width:3.5px;height:3.5px;border-radius:50%;background:var(--paper)}
.side-list b{font-weight:600}
.side-list--tight li{margin-bottom:5.5px}

/* main column */
.main-tab{position:absolute;left:217px;height:19px;background:var(--navy);border-radius:0 10px 10px 0;color:var(--paper);font-weight:700;font-size:11.4px;line-height:19px;padding-left:8px;letter-spacing:.2px}
.timeline{position:absolute;left:221px;width:0;border-left:1px solid #6d7282}
.node{position:absolute;left:218.5px;width:5px;height:5px;border-radius:50%;border:1px solid var(--navy);background:var(--paper)}

.block{position:absolute;left:229px;width:236px;font-size:9px;line-height:11px;color:var(--ink)}
.block h3{font-size:9px;line-height:11px;font-weight:700;color:var(--navy);margin-bottom:1.5px;text-transform:uppercase}
.bullets li{position:relative;padding-left:10px;margin-bottom:3.7px;text-align:justify}
.bullets li::before{content:"";position:absolute;left:1px;top:3px;width:5px;height:5px;border-radius:50%;background:var(--navy)}
.bullets--small li{font-size:7.9px;line-height:9.8px;margin-bottom:5px}
.bullets--small li::before{top:2.5px}
.key{padding-left:10px;font-weight:700;font-size:8.6px;line-height:10.9px}
.role-title{font-size:10.6px;line-height:12px;font-weight:700;color:var(--ink)}
.job-head{display:flex;justify-content:space-between;align-items:baseline;border-bottom:1px solid var(--rule);padding-bottom:.5px;margin-bottom:3.5px}
.job-head .company{font-weight:700;font-size:9.4px;line-height:11px}
.date{font-style:italic;font-weight:600;font-size:7.6px}
.employer{font-weight:700;font-size:10.4px;line-height:12px;color:var(--ink)}
.sub-role{font-weight:700;font-size:8.8px;line-height:11px}

/* page two sidebar */
.sb-title{position:absolute;left:26px;color:var(--paper);font-weight:600;font-size:12.6px;line-height:14px;letter-spacing:.2px}
.sb-list{position:absolute;left:26px;width:162px;border-left:1px dotted var(--muted);padding-left:6.5px;color:var(--light);font-size:9.8px;line-height:12px;font-weight:300}
.sb-list li{position:relative;margin-bottom:11.5px}
.sb-list li::before{content:"";position:absolute;left:-8.7px;top:4px;width:3.5px;height:3.5px;border-radius:50%;background:var(--paper)}
.sb-list b{font-weight:600;margin-right:5px}
.sb-rule{position:absolute;left:26px;width:156px;border-top:1px solid #5d6478}

.activity-box{position:absolute;left:26.5px;top:282.5px;width:154px;height:206px;border:1px solid var(--light);border-radius:2px}
.act-section{position:absolute;left:0;width:100%;border-top:1px solid var(--light)}
.act-label{position:absolute;left:6px;width:140px;color:var(--paper);font-weight:600;font-size:8.8px;line-height:10px;display:flex;gap:2px}
.act-label::after{content:"";flex:1;border-bottom:1px dotted var(--muted);margin-bottom:2px}
.act-label::before{content:"";position:absolute;left:-8px;top:3px;width:3.5px;height:3.5px;border-radius:50%;background:var(--paper)}
.act-row{position:absolute;left:2px;width:150px;display:flex}
.act-item{flex:1;display:flex;flex-direction:column;align-items:center;gap:4px;color:var(--paper);font-size:9.4px;line-height:10px;border-left:1px dotted var(--muted)}
.act-item:first-child{border-left:none}
.act-icon{width:17px;height:17px;border-radius:50%;background:#5a6275}
.piano{position:absolute;left:6px;top:24px;display:flex;align-items:center;gap:16px;color:var(--paper);font-size:9.6px}
.piano .act-icon{width:26px;height:22px;border-radius:3px}
</style>
</head>
<body>

<!-- ============ PAGE ONE ============ -->
<section class="page page--one">
  <div class="portrait-ring"><div class="portrait" role="img" aria-label="Portrait photo of Marcus Vellinger in a dark blazer"></div></div>
  <h1 class="name">MARCUS VELLINGER</h1>

  <div class="side-tab" style="top:229px">PERSONAL INFOS</div>
  <div class="info-row" style="top:255px">
    <svg viewBox="0 0 10 10"><circle cx="5" cy="5" r="5" fill="#eef0f4"/><rect x="2.5" y="3" width="5" height="4.5" fill="none" stroke="#333a4b" stroke-width=".8"/><line x1="2.5" y1="4.4" x2="7.5" y2="4.4" stroke="#333a4b" stroke-width=".8"/></svg>
    <span>17.03.1971</span></div>
  <div class="info-row" style="top:270px">
    <svg viewBox="0 0 10 10"><circle cx="5" cy="5" r="5" fill="#eef0f4"/><path d="M5 2.2a1.8 1.8 0 0 1 1.8 1.8C6.8 5.4 5 7.8 5 7.8S3.2 5.4 3.2 4A1.8 1.8 0 0 1 5 2.2z" fill="#333a4b"/></svg>
    <span>Lindenweg 12<br>50667 Bonn, Germany</span></div>
  <div class="info-row" style="top:295px">
    <svg viewBox="0 0 10 10"><circle cx="5" cy="5" r="5" fill="#eef0f4"/><rect x="2.4" y="3.2" width="5.2" height="3.6" fill="none" stroke="#333a4b" stroke-width=".8"/><path d="M2.4 3.2 5 5.3 7.6 3.2" fill="none" stroke="#333a4b" stroke-width=".8"/></svg>
    <span>marcus.vellinger@mailbox.net</span></div>
  <div class="info-row" style="top:311px">
    <svg viewBox="0 0 10 10"><circle cx="5" cy="5" r="5" fill="#eef0f4"/></svg>
    <span>www.profilehub.net/in/marcusvellinger</span></div>

  <div class="side-tab" style="top:345.5px">QUALIFICATIONS</div>
  <h2 class="side-head" style="top:369px">CORE COMPETENCIES</h2>
  <ul class="side-list" style="top:383px">
    <li><b>Passionate Digital Transformation Leader</b> with track record of launching and growing business</li>
    <li><b>Entrepreneurial background</b> with network to global innovation hubs</li>
    <li><b>Strong Product &amp; Innovation competence</b> with a clear understanding of market needs</li>
    <li><b>Track record in driving partnerships</b> into highly successful collaborations</li>
  </ul>
  <h2 class="side-head" style="top:532px">ACCOMPLISHMENTS</h2>
  <ul class="side-list side-list--tight" style="top:545.5px">
    <li>Mentor at Corvex’s Ignite program for start-ups</li>
    <li>Crash Course in Data Science at The Ashford University</li>
    <li>Intro to Blockchain Technology at Lerin Institute</li>
    <li>PSM 1, Certified Scrum Master, Agile Guild</li>
    <li>Leadership Excellence Program at Calder Business School</li>
  </ul>

  <div class="sheet"></div>

  <div class="main-tab" style="top:26.5px;width:176px">PROFILE &amp; ACHIEVEMENTS</div>
  <div class="timeline" style="top:54px;height:302px"></div>
  <span class="node" style="top:54px"></span>
  <span class="node" style="top:138.5px"></span>
  <span class="node" style="top:265.5px"></span>

  <div class="block" style="top:51px">
    <h3>Guiding Entrepreneurial Innovations</h3>
    <ul class="bullets">
      <li>Define a way forward for Vantelo’s Messaging business</li>
      <li>Shape a venture for Norvik Group in the eMobilty segment</li>
      <li>Build a joint venture of Nordtel and Optrel for the development of connected smart glasses</li>
    </ul>
  </div>
  <div class="block" style="top:135.5px">
    <h3>Leading Global Partnership Networks</h3>
    <ul class="bullets">
      <li>Overcome strategic objectives and forman alliance of Searchly and Vantelo in Messaging</li>
      <li>Position Nordtel as first choice for Orchard smartphones with a purchase volume of more than 2 billion euro</li>
      <li>Create exclusive advantages for Nordtel customers through partnerships with major innovators like Orchard and Rivermart</li>
    </ul>
  </div>
  <div class="block" style="top:262.5px">
    <h3>Delivery-Oriented Product Leader</h3>
    <ul class="bullets">
      <li>Manage the roll out of new GSM-R Units to &gt;5000 vehicles for Federal Rail in logistics and technical integration</li>
      <li>Open the door for IoT business of Sigmalink to access European telcos</li>
      <li>Develop a consistent Aurora@homeexperience and build the corresponding device portfolio supporting DSL, TV, Smart Home</li>
    </ul>
  </div>

  <div class="main-tab" style="top:388px;width:178px">EXPERIENCE (EXEMPLARY)</div>
  <div class="timeline" style="top:416px;height:256px"></div>
  <span class="node" style="top:415.5px"></span>

  <div class="block" style="top:412px"><p class="role-title">SENIOR ADVISOR (self-employed)</p></div>
  <div class="block" style="top:426px">
    <div class="job-head"><span class="company">Incuvate Corporate Startups</span><span class="date">10/2020 – Present</span></div>
    <ul class="bullets">
      <li>Venture building (e.g. with Norvik Group and NT)</li>
      <li style="margin-bottom:0">Derive a product strategy and go to market plan</li>
    </ul>
    <p class="key">Key Success:</p>
    <ul class="bullets"><li>Successful start of Voltra, the Norvik eMobility venture</li></ul>
  </div>
  <div class="block" style="top:507px">
    <div class="job-head"><span class="company">Sigmalink Communications</span><span class="date">08/2021 – Present</span></div>
    <ul class="bullets">
      <li>Define a strategy how to approach telco carriers</li>
      <li style="margin-bottom:2px">Evaluate business models to engage with distributors</li>
    </ul>
    <p class="key">Key Success:</p>
    <ul class="bullets"><li>Growth through new distribution channels via carriers</li></ul>
  </div>
  <div class="block" style="top:592px">
    <div class="job-head"><span class="company">Vantelo</span><span class="date">04/2021 – 04/2022</span></div>
    <ul class="bullets">
      <li>Evaluation of the global messaging business</li>
      <li>Define a new strategy for messaging in Vantelo</li>
      <li style="margin-bottom:0">Implement a new independent business unit for SaaS</li>
    </ul>
    <p class="key">Key Success:</p>
    <ul class="bullets"><li>Successful start of the new business unit</li></ul>
  </div>
</section>

<!-- ============ PAGE TWO ============ -->
<section class="page page--two">
  <h2 class="sb-title" style="top:24px">UNIVERSITY</h2>
  <ul class="sb-list" style="top:39px">
    <li>Executive Leadership Development Program at Westbrook Graduate School of Business (2016)</li>
    <li>Diploma in Electrical Engineering at Technische Hochschule Rheinfeld (THR) (1987-1994)</li>
  </ul>
  <div class="sb-rule" style="top:144px"></div>

  <h2 class="sb-title" style="top:166px">LANGUAGES</h2>
  <ul class="sb-list" style="top:183px">
    <li style="margin-bottom:8px"><b>German</b> Native</li>
    <li><b>English</b> Full professional proficiency</li>
  </ul>
  <div class="sb-rule" style="top:240px"></div>

  <h2 class="sb-title" style="top:262.5px">ACTIVITIES</h2>
  <div class="activity-box">
    <div class="act-label" style="top:8px">SPORT:</div>
    <div class="act-row" style="top:22px">
      <div class="act-item"><span class="act-icon" role="img" aria-label="Skiing icon"></span>Skiing</div>
      <div class="act-item"><span class="act-icon" role="img" aria-label="Tennis icon"></span>Tennis</div>
      <div class="act-item"><span class="act-icon" role="img" aria-label="Hiking icon"></span>Hiking</div>
      <div class="act-item"><span class="act-icon" role="img" aria-label="Yoga icon"></span>Yoga</div>
    </div>
    <div class="act-section" style="top:70px;height:65px">
      <div class="act-label" style="top:8px">MUSIC:</div>
      <div class="piano"><span class="act-icon" role="img" aria-label="Grand piano icon"></span>Classical Piano</div>
    </div>
    <div class="act-section" style="top:134.5px;height:70px">
      <div class="act-label" style="top:10px">TRAVELLING:</div>
      <div class="act-row" style="top:25px">
        <div class="act-item"><span class="act-icon" role="img" aria-label="Map outline of Europe"></span>Europe</div>
        <div class="act-item"><span class="act-icon" role="img" aria-label="Map outline of Africa"></span>Africa</div>
        <div class="act-item"><span class="act-icon" role="img" aria-label="Map outline of America"></span>America</div>
      </div>
    </div>
  </div>
  <div class="sb-rule" style="top:515px"></div>

  <h2 class="sb-title" style="top:539px">REFERENCES</h2>
  <ul class="sb-list" style="top:555px">
    <li>Tobias Hellmann, CEO Nordtel</li>
    <li>Martin Haberland, SVP Global Strategic Projects and Marketing Partnerships, Nordtel</li>
    <li>Yann Mercier, formerly CEO Helix Corporation</li>
  </ul>

  <div class="sheet"></div>

  <div class="timeline" style="top:26px;height:649px"></div>
  <span class="node" style="top:107px"></span>
  <span class="node" style="top:457.5px"></span>

  <div class="block" style="top:22.5px">
    <div class="job-head"><span class="company">Meridian Advisory</span><span class="date">10/2020 – 12/2022</span></div>
    <ul class="bullets"><li style="margin-bottom:6px">Steering of a group wide exchange of GSM-R equipment</li></ul>
    <p class="key">Key Success:</p>
    <ul class="bullets"><li>Improvement of the mobile connectivity experience for customers of the Federal Rail</li></ul>
  </div>

  <div class="block" style="top:103.5px">
    <p class="employer">NORDTEL AG, BONN</p>
    <p class="sub-role" style="margin-top:3.5px">Senior Vice</p>
    <div class="job-head"><span class="company">President Connected Devices</span><span class="date">08/2011 – 07/2020</span></div>
    <ul class="bullets">
      <li>Management of the global partnerships with Orchard, Searchly, Kessan</li>
      <li>Board member of Lumen Inc, a JV of NT and Optrel AG</li>
      <li style="margin-bottom:1px">Driving the entire portfolio of devices for the NT group including Wearables, Voice Controlled Devices and Virtual Reality Glasses</li>
    </ul>
    <p class="key">Key Success:</p>
    <ul class="bullets bullets--small">
      <li>Managing a turnover of more than 3&nbsp;billion euros with devices across the Nordtel group</li>
      <li>Development of the first Aurora Voice Speaker</li>
      <li>Foundation of the Lumenjoint venture</li>
    </ul>
  </div>

  <div class="block" style="top:307px">
    <p class="sub-role">Vice President</p>
    <div class="job-head"><span class="company">Product Management Mobile</span><span class="date">04/2008 –07/2011</span></div>
    <ul class="bullets">
      <li>Introduction of the international portfolio of mobile phones in Nordtel</li>
      <li style="margin-bottom:2px">Project lead for key initiatives, e.g. introduction of Novadroid</li>
    </ul>
    <p class="key">Key Success:</p>
    <ul class="bullets">
      <li>Successful introduction of the first Novadroid phone in an exclusive partnership with Searchly and Helix</li>
      <li>Development of the NT App portfolio for OrchardOS and Novadroid</li>
    </ul>
  </div>

  <div class="block" style="top:454px">
    <div style="display:flex;justify-content:space-between;align-items:baseline"><span class="employer">TELEWAVE INTERNATIONAL, BONN</span><span class="date">09/1994 – 03/2008</span></div>
    <p class="sub-role" style="margin-top:2px">Head of Client Integration/ISP Products</p>
    <ul class="bullets">
      <li>Conception and development of an own-branded mobile phone</li>
      <li>Transformation of product management from voice-centric into mobile internet business</li>
    </ul>
  </div>

  <div class="block" style="top:546.5px">
    <p class="sub-role">Project Lead Personal Communication Services</p>
    <ul class="bullets"><li>Project lead of the first FMC product combining fixed and mobile communication on one bill with one device and one service</li></ul>
  </div>

  <div class="block" style="top:608.5px">
    <p class="sub-role">Project Engineering</p>
    <ul class="bullets">
      <li>Project lead “Short Message Service Center”</li>
      <li>Voice quality assurance: Design of a new measurement system and implementation in C++</li>
      <li>Audits of system technology suppliers</li>
    </ul>
  </div>
</section>

</body>
</html>
```